Diet Pancakes Packaging Design Project

NEW SHORT BRIEF WITH THE OLD BRIEF BELOW (IN CASE OF ANY CONFUSION WITH PREVIOUS DESIGNER INPUT).

IN SHORT -
New packaging for diet meal replacement batter mix to be labelled as 'Protein Pancakes'.
It needs to mention that it can also make the other 5 meal types (muffins, donuts, crepes, pizza base,waffles).
The 2 main cooking purposes are waffles and pancakes (in case both can be shown on the front of the box).
The boxes must mention - gluten free, fat free (no saturated fat), carb free (zero nett carb)with added fat burners and carb blockers.
6 flavours (vanilla, berry, banana, cheese, apple cinnamon, choc coconut).
WE HAD AN IDEA THAT WE LIKED WHERE A 2-PART BOX WITH INNER AND OUTER WAS USED.
INNER TO HAVE SOME BASIC PRINT THAT CAN BE SEEN THROUGH A CUT-OUT ON THE OUTER AS WELL AS UNDER THE OUTER (FLAVOUR AND NUTRITIONAL PANEL AT REAR).
INNER CAN BE A DIFFERENT COLOUR FOR EACH FLAVOUR.
THE CONCEPT CAB BE SEEN IN THE IMAGES ATTACHED.
WE ALSO LIKED THE CONCEPT OF HAVING A PATTERN AS SHOWN ON THE BAG IMAGE ATTACHED FOR THE SIDE OF THE BOXES WHICH CAN BE CARRIED ON INTO OTHER NEW ARTWORK.

PREVIOUS DESCRIPTION OF REQUIREMENTS -

We need a new box design for our diet pancake batter mix.

We are marketing in 4 areas -
Retail Supermarkets (Gluten Free/Sugar Free)
Pharmacy/Chemists (Fat Loss/Detox)
Health Food Stores (Gluten Free/Carb Free/Fat Loss)
Supplement Stores (Muscle Building)

Our product is suitable for all requirements (gluten free, carb free, fat free, high fibre (suitable for detox), high protein (for muscle gain or as a meal replacement), added fat burners, carb lockers and appetite suppressants (fat loss).

Our original packaging is minimal showcasing all the different meals that can be made with the one batter mix (see images attached).
Each side of the box had a different meal option.
We have 3 sweet flavours so they were all the same except for the mentioning of the flavour on each box and 1 savoury flavour that had 2 different meals (pizza and crepe) replacing donuts and pancakes (as they are not generally made in a savoury flavour).

The issue with current packaging is that -
1. People are not understanding the products.
They think that the meals are ready to eat and not in packets to add water and cook.
2. People want to try before buying a 10 meal
We need a smaller box with mixed flavours or preferably 2 smaller boxs with 3 mixed sweet flavours and one with all 4 flavours.
This can be expanded to have 3 of the same flavours per box also.

The product may also be better to be called a pancake batter mix that also makes the other meals or even a pancake and waffle batter mix as they are the two main meals cooked (with the mention that they can also make muffins etc).

I have attached some current box designs (10 packet meals).
New designs are for 3 and 4 packet meals.
Our web site is www.nordcake.example
(You can see all the boxes there).

Final design must be print ready with all sides of the box approved (Final art line will be provided).

Target Market(s)

Retail Supermarkets (Gluten Free/Sugar Free) Pharmacy/Chemists (Fat Loss/Detox) Health Food Stores (Gluten Free/Carb Free/Fat Loss) Supplement Stores

Industry/Entity Type

Marketing

Requirements
Must have
• Must be targeted at the diet industry, such as Gulten Free, Carb Free and Fat Free being clearly shown on the packaging.

Packaging size preferred to be in keeping with current box designs-
140x140x? (width should either be 1/3 (45) or 1/2 (65), allowing for box thickness to make up the difference to 140 width).

Must show nutritional panel and all other information as currently shown under original boxes (can be anywhere on new box design)
Nice to have
• Would like to see a design that explains what is in the boxes (A diet batter mix that is ready to cook).
With a heading for PROTEIN PANCAKES and another (can be same design) with WEIGHT-LOSS PANCAKES.

Would like to design with a coloured inner box for simple re-packaging with the different outer boxes.
Should not have
• A design that can be utilised for future designs such as a side panel design as shown on attached bag design.
The small boxed images can be of all the different meals it makes in a similar design.
We will be requiring additional promo items including bags and business cards, posters, floor stands, t-shirts, car decals etc.

```html
<!DOCTYPE html>
<html lang="en">
<head>
<meta charset="utf-8">
<title>Diet Pancake Mix – Box Panels</title>
<link rel="stylesheet" href="https://fonts.googleapis.com/css2?family=Roboto+Condensed:wght@400;700&family=Roboto+Slab:wght@700&display=swap">
<style>
  :root{
    --bg:#ffffff;
    --lid:#b9b9bb;
    --lid-edge:#a9a9ab;
    --band:#cfcfd1;
    --ink:#2a2a2e;
    --muted:#5b5b60;
    --brand:#e3245a;
    --panel:#ffffff;
  }
  *{box-sizing:border-box;margin:0;padding:0}
  html,body{width:1200px;height:885px;overflow:hidden;background:var(--bg)}
  body{font-family:"Roboto Condensed",Arial,sans-serif;color:var(--ink);position:relative}

  .box{position:absolute;top:150px;width:530px;height:590px}
  .box--mixed{left:50px}
  .box--classic{left:620px}

  .lid{position:absolute;left:270px;top:0;width:260px;height:260px;background:var(--lid);
       border:1px solid var(--lid-edge);display:flex;align-items:center;justify-content:center}

  .brand{display:flex;align-items:center;gap:5px;font-family:"Roboto Condensed",Arial,sans-serif;
         font-weight:700;font-size:13px;line-height:1;color:var(--brand)}
  .brand__mark{width:10px;height:10px;background:var(--brand);display:inline-block;flex:none}

  .face{position:absolute;top:270px;width:260px;height:260px;background:var(--panel);
        border:1px solid #d8d8da;overflow:hidden}
  .face--side{left:0}
  .face--front{left:270px}

  .band{height:30px;background:var(--band);font-size:9px;font-weight:700;text-transform:uppercase;
        letter-spacing:.5px;color:var(--muted);display:flex;align-items:center;padding:0 10px;white-space:nowrap}

  .copy{position:absolute;left:12px;top:42px;width:200px}
  .title{font-family:"Roboto Slab",Georgia,serif;font-weight:700;font-size:20px;line-height:1.1;
         color:var(--ink);white-space:nowrap}
  .subtitle{margin-top:6px;font-size:10px;font-weight:700;line-height:1.25;color:var(--muted)}
  .note{margin-top:8px;font-size:8px;line-height:1.2;color:var(--muted);white-space:nowrap}

  .tab{position:absolute;right:0;top:30px;width:30px;height:98px;background:var(--brand);
       display:flex;flex-direction:column;align-items:center;padding-top:8px;gap:8px}
  .tab__badge{width:18px;height:14px;background:#fff;flex:none}
  .tab__text{writing-mode:vertical-rl;transform:rotate(180deg);color:#fff;font-size:7.5px;
             font-weight:700;text-transform:uppercase;letter-spacing:.5px;white-space:nowrap}

  .photo{position:absolute;left:0;right:0;bottom:0;height:130px}
  .photo--waffle{background:radial-gradient(circle at 30% 40%,#7a2a3c 0 14%,transparent 30%),linear-gradient(135deg,#d99a4a,#b9732e 60%,#e9c79a)}
  .photo--muffin{background:radial-gradient(circle at 70% 45%,#e8b75a 0 25%,transparent 45%),linear-gradient(160deg,#f1f3f7,#d9a658 55%,#7fa0cf)}
  .photo--pastry{background:radial-gradient(circle at 40% 40%,#f3d7c4 0 22%,transparent 40%),linear-gradient(135deg,#e9b49a,#c9823f 60%,#f4e2cf)}
  .photo--pancake{background:radial-gradient(circle at 30% 70%,#c9272f 0 10%,transparent 20%),radial-gradient(circle at 65% 50%,#e7a24a 0 28%,transparent 45%),linear-gradient(160deg,#ffffff,#f2d3a0 70%)}
</style>
</head>
<body>

<section class="box box--mixed" aria-label="Mixed meals box">
  <div class="lid"><span class="brand"><span class="brand__mark"></span>Nordcake</span></div>

  <article class="face face--side">
    <div class="band">Gluten free · Carb free · Fat free</div>
    <div class="copy">
      <h2 class="title">Diet Pancake Mix</h2>
      <p class="subtitle">Makes pancakes, waffles, muffins, crepes and donuts</p>
      <p class="note">Just add water &amp; cook</p>
    </div>
    <div class="tab"><span class="tab__badge"></span><span class="tab__text">Fat burner</span></div>
    <div class="photo photo--waffle" role="img" aria-label="Photo of a waffle topped with berries and cream"></div>
  </article>

  <article class="face face--front">
    <div class="band">Gluten free · Carb free · Fat free</div>
    <div class="copy">
      <h2 class="title">Diet Pancake Mix</h2>
      <p class="subtitle">Makes pancakes, waffles, muffins, crepes and donuts</p>
      <p class="note">Just add water &amp; cook</p>
    </div>
    <div class="tab"><span class="tab__badge"></span><span class="tab__text">Fat burner</span></div>
    <div class="photo photo--muffin" role="img" aria-label="Photo of berry muffins with cherries"></div>
  </article>
</section>

<section class="box box--classic" aria-label="Pancake box">
  <div class="lid"><span class="brand"><span class="brand__mark"></span>Nordcake</span></div>

  <article class="face face--side">
    <div class="band">Gluten free · Carb free · Fat free</div>
    <div class="copy">
      <h2 class="title">Diet Pancake Mix</h2>
      <p class="subtitle">Makes pancakes, waffles, muffins, crepes and donuts</p>
      <p class="note">www.nordcake.example</p>
    </div>
    <div class="tab"><span class="tab__badge"></span><span class="tab__text">Fat burner</span></div>
    <div class="photo photo--pastry" role="img" aria-label="Photo of sugared donut puffs"></div>
  </article>

  <article class="face face--front">
    <div class="band">Gluten free · Carb free · Fat free</div>
    <div class="copy">
      <h2 class="title">Diet Pancake Mix</h2>
      <p class="subtitle">Makes pancakes, waffles, muffins, crepes and donuts</p>
      <p class="note">Just add water &amp; cook</p>
    </div>
    <div class="tab"><span class="tab__badge"></span><span class="tab__text">Fat burner</span></div>
    <div class="photo photo--pancake" role="img" aria-label="Photo of a pancake stack with syrup and strawberries"></div>
  </article>
</section>

</body>
</html>
```